Cardboard hanging box designs

I need to get some cardboard boxes made up for trailer wheel bearing kits. They need to be hanging boxes as pictured. The box needs to fit with our existing colour scheme and be clearly evident that it is for trailers. I am after 2 designs, one for "Trailer Bearing Kit" and one for "Marine Bearing Kit".
The Marine Bearing kit box should measure, 180mm High, 120mm Wide, 60mm Deep.
The Trailer Bearing kit box should measure, 180mm high, 120mm Wide, 30mm Deep.
These are all external measurements.

```html
<!DOCTYPE html>
<html lang="en">
<head>
<meta charset="UTF-8">
<title>Trailer Bearing Kit – Hanging Box</title>
<link href="https://fonts.googleapis.com/css2?family=Barlow+Condensed:ital,wght@0,600;0,700;1,700&display=swap" rel="stylesheet">
<style>
  :root {
    --bg: #d9d9d9;
    --red: #8f1015;
    --red-dark: #6a0a0e;
    --red-bright: #b0161d;
    --white: #ffffff;
    --yellow: #f7dc3b;
    --ink: #111111;
    --steel-light: #c9c9c9;
    --steel-dark: #6f6f6f;
  }
  html, body {
    margin: 0;
    width: 1200px;
    height: 750px;
    overflow: hidden;
    background: var(--bg);
    font-family: "Barlow Condensed", sans-serif;
  }
  .canvas { position: relative; width: 1200px; height: 750px; }

  /* hang tab */
  .hang-tab { position: absolute; left: 430px; top: 40px; width: 360px; height: 110px; }

  /* side panel */
  .side-panel {
    position: absolute; left: 340px; top: 150px; width: 90px; height: 540px;
    background: var(--white); overflow: hidden;
  }
  .side-panel .band-top { position: absolute; inset: 0 0 auto 0; height: 14px; background: var(--red-dark); }
  .side-panel .band-bottom { position: absolute; left: 0; top: 0; width: 90px; height: 540px; }
  .sets-badge {
    position: absolute; left: 10px; top: 14px; width: 60px; height: 74px;
    background: linear-gradient(160deg, var(--red-bright), var(--red-dark));
    color: var(--white); text-align: center; font-weight: 700; line-height: 1;
  }
  .sets-badge .count { display: block; font-size: 44px; padding-top: 6px; }
  .sets-badge .label { display: block; font-size: 15px; }
  .side-brand {
    position: absolute; left: 0; right: 0; top: 240px; text-align: center;
    font-weight: 700; font-size: 15px; color: var(--ink); letter-spacing: 0.3px;
  }
  .side-icon {
    position: absolute; left: 28px; top: 418px; width: 34px; height: 34px; border-radius: 50%;
    background: radial-gradient(circle, rgba(255,255,255,0.2) 30%, rgba(255,255,255,0.75) 32%, rgba(255,255,255,0.75) 48%, rgba(255,255,255,0.15) 50%);
  }
  .side-title {
    position: absolute; left: 0; right: 0; top: 462px; text-align: center;
    color: var(--white); font-weight: 600; font-size: 19px; line-height: 1.05;
  }

  /* front panel */
  .front-panel {
    position: absolute; left: 430px; top: 150px; width: 360px; height: 540px;
    background: var(--white); overflow: hidden;
  }
  .front-panel .art { position: absolute; inset: 0; }
  .brand-name {
    position: absolute; left: 0; right: 0; top: 70px; text-align: center;
    font-weight: 700; font-size: 64px; color: var(--ink); letter-spacing: 2px; line-height: 1;
  }
  .product-photo {
    position: absolute; left: 95px; top: 145px; width: 175px; height: 180px; border-radius: 50%;
    background: radial-gradient(ellipse at 50% 50%, var(--white) 38%, var(--steel-light) 44%, var(--steel-dark) 58%, var(--steel-light) 68%, rgba(201,201,201,0) 71%);
  }
  .title-block {
    position: absolute; left: 22px; top: 398px; width: 330px;
    transform: rotate(-12.5deg); transform-origin: left top; color: var(--white);
  }
  .product-title { margin: 0 0 6px; font-weight: 700; font-size: 38px; letter-spacing: 0.5px; line-height: 1; }
  .feature-list { list-style: none; margin: 0; padding: 0; }
  .feature-list li {
    position: relative; padding-left: 26px; margin-bottom: 4px;
    font-weight: 700; font-style: italic; font-size: 12.5px; line-height: 1.15; letter-spacing: 0.4px;
  }
  .feature-list svg { position: absolute; left: 0; top: 2px; width: 18px; height: 18px; }
</style>
</head>
<body>
<div class="canvas">

  <svg class="hang-tab" viewBox="0 0 360 110" aria-hidden="true">
    <defs>
      <linearGradient id="tabFill" x1="0" y1="0" x2="0" y2="1">
        <stop offset="0" stop-color="#8f1015"/>
        <stop offset="1" stop-color="#7a0c10"/>
      </linearGradient>
    </defs>
    <rect x="0" y="0" width="360" height="110" fill="url(#tabFill)"/>
    <path d="M163 48 h12 a12 12 0 0 1 24 0 h12 a9 9 0 0 1 0 18 h-48 a9 9 0 0 1 0 -18 z" fill="var(--bg)"/>
  </svg>

  <section class="side-panel">
    <svg class="band-bottom" viewBox="0 0 90 540" aria-hidden="true">
      <polygon points="0,395 90,380 90,540 0,540" fill="var(--red)"/>
    </svg>
    <div class="band-top"></div>
    <div class="sets-badge"><span class="count">2</span><span class="label">SETS</span></div>
    <div class="side-brand">KORVA PARTS</div>
    <div class="side-icon" role="img" aria-label="Bearing icon"></div>
    <div class="side-title">Trailer<br>Bearing<br>Kit</div>
  </section>

  <section class="front-panel">
    <svg class="art" viewBox="0 0 360 540" aria-hidden="true">
      <rect x="0" y="0" width="360" height="22" fill="var(--red-dark)"/>
      <polygon points="360,230 360,300 170,342" fill="var(--yellow)"/>
      <polygon points="0,380 360,300 360,540 0,540" fill="var(--red)"/>
    </svg>
    <div class="brand-name">KORVA PARTS</div>
    <div class="product-photo" role="img" aria-label="Photo of a tapered roller bearing with its race"></div>
    <div class="title-block">
      <h1 class="product-title">TRAILER BEARING KIT</h1>
      <ul class="feature-list">
        <li><svg viewBox="0 0 18 18"><path d="M2 10 L7 15 L16 2" fill="none" stroke="#fff" stroke-width="2.4"/></svg>HEAVY DUTY BEARINGS FOR EXTENDED SERVICE LIFE</li>
        <li><svg viewBox="0 0 18 18"><path d="M2 10 L7 15 L16 2" fill="none" stroke="#fff" stroke-width="2.4"/></svg>PRECISION ENGINEERED BEARING RACES PROVIDE MAXIMUM LOAD CAPACITY</li>
        <li><svg viewBox="0 0 18 18"><path d="M2 10 L7 15 L16 2" fill="none" stroke="#fff" stroke-width="2.4"/></svg>HIGH QUALITY OIL SEALS ELIMINATE BEARING CONTAMINATION</li>
      </ul>
    </div>
  </section>

</div>
</body>
</html>
```